We need a business card design for our residential home building company based out of East Tennessee and the Smoky Mountains. We have 30 years of experience, and we plan to build homes not only in the state of Tennessee, but out of state as well. We are a different kind of production home builder; we aim to build homes cost-effectively and efficiently but with the character, dignity, and charm of historic homes. Our homes have a timeless style with modern floorplans and features. We would like to see designs that embody a classic style with accents of gold, red, and blue. The resulting business card should convey elegance, strength, character, and trust as well as the careful balance of the old and new.
Motto: "Building Your Legacy"
Target Market(s)
Adults 40+ from the Northern states looking to settle in Tennessee.
Industry/Entity Type
Residential
Contact Information for Business Card
Birchline Dwellworks, LLC
Marisol Thackett | Director of Operations
24815 Quarrybend Lane | Suite 500
Fernwick Falls, OR 48261
Office: (555)314-2290
Mobile: (555)648-1173
Email: marisol@birchlinedwellworks.example

```html
<!DOCTYPE html>
<html lang="en">
<head>
<meta charset="utf-8">
<title>Birchline Dwellworks – Business Card</title>
<link href="https://fonts.googleapis.com/css2?family=Libre+Baskerville:ital,wght@0,400;0,700;1,400&family=Courgette&family=Open+Sans:wght@700;800&display=swap" rel="stylesheet">
<style>
:root{
  --bg:#e6e4e0;
  --cream:#fdf7dc;
  --cream-2:#fbeeb8;
  --gold:#f9d35a;
  --gold-deep:#f4c233;
  --brown:#7a6442;
  --text:#6b6152;
  --red:#d31f2b;
  --blue:#2f6fb9;
  --tile:#fbe59a;
}
*{margin:0;padding:0;box-sizing:border-box}
html,body{width:1200px;height:1200px;overflow:hidden;background:var(--bg)}
.canvas{position:relative;width:1200px;height:1200px}
.card{position:absolute;left:240px;width:720px;height:420px;overflow:hidden;box-shadow:0 6px 18px rgba(0,0,0,.25)}
.card-front{top:100px;background:linear-gradient(180deg,var(--cream) 0%,var(--cream-2) 60%)}
.card-back{top:680px;background:radial-gradient(ellipse at 70% 40%,var(--gold-deep) 0%,var(--gold) 55%,#fce27f 100%)}

.front-wave{position:absolute;inset:0}
.brand{position:absolute;left:66px;top:150px;width:220px;display:flex;align-items:center;gap:12px}
.brand-mark{flex:none;width:26px;height:26px;border:3px solid var(--brown)}
.brand-name{font-family:"Libre Baskerville",serif;font-weight:700;font-size:22px;line-height:1.3;color:var(--brown)}
.motto{position:absolute;left:36px;top:322px;font-family:"Courgette",cursive;font-size:22px;color:#6e5c34}

.person{position:absolute;right:38px;top:64px;text-align:right;font-family:"Libre Baskerville",serif}
.person-name{font-weight:700;font-size:25px;color:var(--red)}
.person-title{font-style:italic;font-size:18px;color:var(--text);margin-top:6px}
.address{position:absolute;right:38px;top:192px;text-align:right;font-family:"Libre Baskerville",serif;font-size:19px;line-height:1.55;color:var(--text);font-style:normal}
.contacts{position:absolute;right:38px;top:270px;list-style:none;font-family:"Libre Baskerville",serif;font-size:19px;color:var(--text)}
.contacts li{display:flex;justify-content:flex-end;align-items:center;gap:12px;height:40px}
.contacts svg{fill:var(--brown)}

.year{position:absolute;left:14px;top:44px;writing-mode:vertical-rl;transform:rotate(180deg);font-family:"Libre Baskerville",serif;font-weight:700;font-size:20px;color:var(--blue)}
.months{position:absolute;left:54px;top:24px;display:grid;grid-template-columns:repeat(4,146px);grid-auto-rows:114px;column-gap:16px;row-gap:14px}
.month{background:linear-gradient(160deg,#fdf0c0,var(--tile));border:1.5px solid #c9d3e0;border-radius:14px 4px 14px 4px;padding:10px 14px 0;font-family:"Open Sans",sans-serif;color:var(--blue)}
.month h3{font-size:10.5px;font-weight:800;text-align:center;letter-spacing:.3px;margin-bottom:5px}
.week,.days{list-style:none;display:grid;grid-template-columns:repeat(7,1fr);text-align:center}
.week{font-size:5.5px;font-weight:700;color:#455a78;margin-bottom:2px}
.days{font-size:7.5px;font-weight:700;line-height:11.5px}
.days li:first-child{grid-column-start:var(--start)}
</style>
</head>
<body>
<main class="canvas">

  <section class="card card-front" aria-label="Business card front">
    <svg class="front-wave" width="720" height="420" viewBox="0 0 720 420" aria-hidden="true">
      <defs>
        <linearGradient id="band" x1="0" y1="0" x2="1" y2="1">
          <stop offset="0" stop-color="#fce38a"/>
          <stop offset=".5" stop-color="#f8cf4a"/>
          <stop offset="1" stop-color="#fbe07c"/>
        </linearGradient>
        <linearGradient id="rule" x1="0" x2="1">
          <stop offset="0" stop-color="#d31f2b"/>
          <stop offset=".6" stop-color="#e8731f"/>
          <stop offset="1" stop-color="#f6b43a"/>
        </linearGradient>
      </defs>
      <path d="M0 262 Q190 300 360 258 L720 253 L720 420 L0 420Z" fill="url(#band)"/>
      <path d="M285 266 Q320 258 360 257 L720 252" fill="none" stroke="url(#rule)" stroke-width="3"/>
    </svg>

    <div class="brand">
      <span class="brand-mark"></span>
      <span class="brand-name">Birchline Dwellworks, LLC</span>
    </div>
    <p class="motto">Building Your Legacy</p>

    <header class="person">
      <h1 class="person-name">Marisol Thackett</h1>
      <p class="person-title">Director of Operations</p>
    </header>

    <address class="address">
      24815 Quarrybend Lane, Suite 500<br>
      Fernwick Falls, OR 48261
    </address>

    <ul class="contacts">
      <li>
        <svg width="18" height="18" viewBox="0 0 24 24" aria-hidden="true"><path d="M6.6 10.8a15.1 15.1 0 0 0 6.6 6.6l2.2-2.2a1 1 0 0 1 1-.25 11.4 11.4 0 0 0 3.6.57 1 1 0 0 1 1 1V20a1 1 0 0 1-1 1A17 17 0 0 1 3 4a1 1 0 0 1 1-1h3.5a1 1 0 0 1 1 1c0 1.25.2 2.45.57 3.57a1 1 0 0 1-.25 1z"/></svg>
        <span>(555)314-2290</span>
      </li>
      <li>
        <svg width="16" height="24" viewBox="0 0 16 24" aria-hidden="true"><path d="M3 0h10a3 3 0 0 1 3 3v18a3 3 0 0 1-3 3H3a3 3 0 0 1-3-3V3a3 3 0 0 1 3-3zm0 3v15h10V3zm5 16.5a1.5 1.5 0 1 0 0 3 1.5 1.5 0 0 0 0-3z"/></svg>
        <span>(555)648-1173</span>
      </li>
      <li>
        <svg width="18" height="14" viewBox="0 0 18 14" aria-hidden="true"><path d="M0 0h18v2L9 8 0 2zm0 4l9 6 9-6v10H0z"/></svg>
        <span>marisol@birchlinedwellworks.example</span>
      </li>
    </ul>
  </section>

  <section class="card card-back" aria-label="Business card back, 2015 calendar">
    <p class="year">2015</p>
    <div class="months">
      <article class="month"><h3>JANUARY</h3><ul class="week"><li>S</li><li>M</li><li>T</li><li>W</li><li>T</li><li>F</li><li>S</li></ul>
        <ol class="days" style="--start:5"><li>1</li><li>2</li><li>3</li><li>4</li><li>5</li><li>6</li><li>7</li><li>8</li><li>9</li><li>10</li><li>11</li><li>12</li><li>13</li><li>14</li><li>15</li><li>16</li><li>17</li><li>18</li><li>19</li><li>20</li><li>21</li><li>22</li><li>23</li><li>24</li><li>25</li><li>26</li><li>27</li><li>28</li><li>29</li><li>30</li><li>31</li></ol></article>
      <article class="month"><h3>FEBRUARY</h3><ul class="week"><li>S</li><li>M</li><li>T</li><li>W</li><li>T</li><li>F</li><li>S</li></ul>
        <ol class="days" style="--start:1"><li>1</li><li>2</li><li>3</li><li>4</li><li>5</li><li>6</li><li>7</li><li>8</li><li>9</li><li>10</li><li>11</li><li>12</li><li>13</li><li>14</li><li>15</li><li>16</li><li>17</li><li>18</li><li>19</li><li>20</li><li>21</li><li>22</li><li>23</li><li>24</li><li>25</li><li>26</li><li>27</li><li>28</li></ol></article>
      <article class="month"><h3>MARCH</h3><ul class="week"><li>S</li><li>M</li><li>T</li><li>W</li><li>T</li><li>F</li><li>S</li></ul>
        <ol class="days" style="--start:1"><li>1</li><li>2</li><li>3</li><li>4</li><li>5</li><li>6</li><li>7</li><li>8</li><li>9</li><li>10</li><li>11</li><li>12</li><li>13</li><li>14</li><li>15</li><li>16</li><li>17</li><li>18</li><li>19</li><li>20</li><li>21</li><li>22</li><li>23</li><li>24</li><li>25</li><li>26</li><li>27</li><li>28</li><li>29</li><li>30</li><li>31</li></ol></article>
      <article class="month"><h3>APRIL</h3><ul class="week"><li>S</li><li>M</li><li>T</li><li>W</li><li>T</li><li>F</li><li>S</li></ul>
        <ol class="days" style="--start:4"><li>1</li><li>2</li><li>3</li><li>4</li><li>5</li><li>6</li><li>7</li><li>8</li><li>9</li><li>10</li><li>11</li><li>12</li><li>13</li><li>14</li><li>15</li><li>16</li><li>17</li><li>18</li><li>19</li><li>20</li><li>21</li><li>22</li><li>23</li><li>24</li><li>25</li><li>26</li><li>27</li><li>28</li><li>29</li><li>30</li></ol></article>
      <article class="month"><h3>MAY</h3><ul class="week"><li>S</li><li>M</li><li>T</li><li>W</li><li>T</li><li>F</li><li>S</li></ul>
        <ol class="days" style="--start:6"><li>1</li><li>2</li><li>3</li><li>4</li><li>5</li><li>6</li><li>7</li><li>8</li><li>9</li><li>10</li><li>11</li><li>12</li><li>13</li><li>14</li><li>15</li><li>16</li><li>17</li><li>18</li><li>19</li><li>20</li><li>21</li><li>22</li><li>23</li><li>24</li><li>25</li><li>26</li><li>27</li><li>28</li><li>29</li><li>30</li><li>31</li></ol></article>
      <article class="month"><h3>JUNE</h3><ul class="week"><li>S</li><li>M</li><li>T</li><li>W</li><li>T</li><li>F</li><li>S</li></ul>
        <ol class="days" style="--start:2"><li>1</li><li>2</li><li>3</li><li>4</li><li>5</li><li>6</li><li>7</li><li>8</li><li>9</li><li>10</li><li>11</li><li>12</li><li>13</li><li>14</li><li>15</li><li>16</li><li>17</li><li>18</li><li>19</li><li>20</li><li>21</li><li>22</li><li>23</li><li>24</li><li>25</li><li>26</li><li>27</li><li>28</li><li>29</li><li>30</li></ol></article>
      <article class="month"><h3>JULY</h3><ul class="week"><li>S</li><li>M</li><li>T</li><li>W</li><li>T</li><li>F</li><li>S</li></ul>
        <ol class="days" style="--start:4"><li>1</li><li>2</li><li>3</li><li>4</li><li>5</li><li>6</li><li>7</li><li>8</li><li>9</li><li>10</li><li>11</li><li>12</li><li>13</li><li>14</li><li>15</li><li>16</li><li>17</li><li>18</li><li>19</li><li>20</li><li>21</li><li>22</li><li>23</li><li>24</li><li>25</li><li>26</li><li>27</li><li>28</li><li>29</li><li>30</li><li>31</li></ol></article>
      <article class="month"><h3>AUGUST</h3><ul class="week"><li>S</li><li>M</li><li>T</li><li>W</li><li>T</li><li>F</li><li>S</li></ul>
        <ol class="days" style="--start:7"><li>1</li><li>2</li><li>3</li><li>4</li><li>5</li><li>6</li><li>7</li><li>8</li><li>9</li><li>10</li><li>11</li><li>12</li><li>13</li><li>14</li><li>15</li><li>16</li><li>17</li><li>18</li><li>19</li><li>20</li><li>21</li><li>22</li><li>23</li><li>24</li><li>25</li><li>26</li><li>27</li><li>28</li><li>29</li><li>30</li><li>31</li></ol></article>
      <article class="month"><h3>OCTOBER</h3><ul class="week"><li>S</li><li>M</li><li>T</li><li>W</li><li>T</li><li>F</li><li>S</li></ul>
        <ol class="days" style="--start:5"><li>1</li><li>2</li><li>3</li><li>4</li><li>5</li><li>6</li><li>7</li><li>8</li><li>9</li><li>10</li><li>11</li><li>12</li><li>13</li><li>14</li><li>15</li><li>16</li><li>17</li><li>18</li><li>19</li><li>20</li><li>21</li><li>22</li><li>23</li><li>24</li><li>25</li><li>26</li><li>27</li><li>28</li><li>29</li><li>30</li><li>31</li></ol></article>
      <article class="month"><h3>SEPTEMBER</h3><ul class="week"><li>S</li><li>M</li><li>T</li><li>W</li><li>T</li><li>F</li><li>S</li></ul>
        <ol class="days" style="--start:3"><li>1</li><li>2</li><li>3</li><li>4</li><li>5</li><li>6</li><li>7</li><li>8</li><li>9</li><li>10</li><li>11</li><li>12</li><li>13</li><li>14</li><li>15</li><li>16</li><li>17</li><li>18</li><li>19</li><li>20</li><li>21</li><li>22</li><li>23</li><li>24</li><li>25</li><li>26</li><li>27</li><li>28</li><li>29</li><li>30</li></ol></article>
      <article class="month"><h3>NOVEMBER</h3><ul class="week"><li>S</li><li>M</li><li>T</li><li>W</li><li>T</li><li>F</li><li>S</li></ul>
        <ol class="days" style="--start:1"><li>1</li><li>2</li><li>3</li><li>4</li><li>5</li><li>6</li><li>7</li><li>8</li><li>9</li><li>10</li><li>11</li><li>12</li><li>13</li><li>14</li><li>15</li><li>16</li><li>17</li><li>18</li><li>19</li><li>20</li><li>21</li><li>22</li><li>23</li><li>24</li><li>25</li><li>26</li><li>27</li><li>28</li><li>29</li><li>30</li></ol></article>
      <article class="month"><h3>DECEMBER</h3><ul class="week"><li>S</li><li>M</li><li>T</li><li>W</li><li>T</li><li>F</li><li>S</li></ul>
        <ol class="days" style="--start:3"><li>1</li><li>2</li><li>3</li><li>4</li><li>5</li><li>6</li><li>7</li><li>8</li><li>9</li><li>10</li><li>11</li><li>12</li><li>13</li><li>14</li><li>15</li><li>16</li><li>17</li><li>18</li><li>19</li><li>20</li><li>21</li><li>22</li><li>23</li><li>24</li><li>25</li><li>26</li><li>27</li><li>28</li><li>29</li><li>30</li><li>31</li></ol></article>
    </div>
  </section>

</main>
</body>
</html>
```